Consultant needs a simple webpage with WOW effect

I educate advisors in the financial sector in the use of Konfera, Talkly, ScreenBridge etc. for online customer meetings.
My Company has a name (Vaneo) and a domain (vaneo.dk).
VANEO is VArige NEtOpgaver (digital competences in Danish)
I made a terrible mock up via the editor on plixo.com on the domain. Have a look.
I need my logo to be much better (but I would like to keep the 0II0) and the webpage to be totally re-designed and catchy.
The text is in Danish and the headlines is what, how and who (Hvem, hvad og hvordan).
Ideas for a better structure are welcome :-)

Target Group: Human Ressource, technical developers and business developers in financial Companies. In Denmark we do not have a tradition for very "corporate" looks in the finansial sector. I would like creativity and customer value to be on top of mind.

Task: Redesign the logo, design the web page.

```html
<!DOCTYPE html>
<html lang="en">
<head>
<meta charset="utf-8">
<title>VANEO – Varige netopgaver i kundemødet</title>
<link rel="stylesheet" href="https://fonts.googleapis.com/css2?family=Raleway:wght@400;500;700;800&family=Source+Sans+3:wght@400;600&display=swap">
<style>
:root{
  --orange:#ef7a1a;
  --black:#000;
  --ink:#333;
  --text:#555;
  --muted:#6b6b6b;
  --panel:#f1f1f1;
  --band:#f6f6f6;
  --line:#d3d3d3;
  --footer:#333333;
  --slate:#5d6a73;
  --white:#fff;
}
*{margin:0;padding:0;box-sizing:border-box}
html,body{width:695px;height:1200px;overflow:hidden;background:var(--white)}
body{position:relative;font-family:"Source Sans 3",Arial,sans-serif;color:var(--text)}
.abs{position:absolute}
h1,h2,h3{font-family:"Raleway",Arial,sans-serif;font-weight:500}

/* header */
.site-header{left:0;top:0;width:695px;height:66px;background:var(--black)}
.brand{left:78px;top:11px;display:flex;align-items:center;gap:5px}
.brand-mark{width:7px;height:7px;background:var(--orange)}
.brand-name{font-family:"Raleway",sans-serif;font-weight:800;font-size:23px;color:var(--white);letter-spacing:-.5px;line-height:1}
.brand-tag{left:80px;top:37px;font-family:"Raleway",sans-serif;font-weight:700;font-size:6.4px;line-height:8px;color:var(--white)}
.search{left:496px;top:12px;width:123px;height:19px;border:1px solid #9a9a9a}
.search svg{position:absolute;right:6px;top:4px}
.nav{top:41px;left:316px;display:flex;font-family:"Raleway",sans-serif;font-size:7.6px;color:#ddd;height:25px}
.nav a{display:block;padding:6px 8px 0;text-decoration:none;color:inherit;border-top:1px solid transparent;margin-right:0}
.nav a.active{color:var(--orange);border-top:1px solid var(--orange)}

/* hero */
.hero{left:0;top:66px;width:695px;height:273px;background:linear-gradient(100deg,#c8ccd0 0%,#8d929a 22%,#dfe3e6 45%,#eef0f2 70%,#d9dde0 100%)}
.hero-caption{right:75px;top:173px;display:flex;flex-direction:column;align-items:flex-end;gap:4px}
.hero-caption span{background:rgba(70,70,70,.78);color:var(--white);font-family:"Raleway",sans-serif;font-size:11px;padding:3px 8px;line-height:14px}
.hero-arrow{top:249px;width:20px;height:20px;display:flex;align-items:center;justify-content:center}
.hero-arrow.prev{left:577px;background:var(--slate)}
.hero-arrow.next{left:600px;background:var(--orange)}

/* welcome */
.welcome-title{left:76px;top:375px;font-size:17px;color:var(--ink);font-weight:400}
.welcome-title em{font-style:normal;color:var(--orange)}
.welcome-text{left:76px;top:405px;width:360px;font-size:7.5px;line-height:15px}
.video{left:76px;top:481px;width:354px;height:130px;background:linear-gradient(90deg,#c5ccd3 0%,#e8ecef 35%,#b0b8c2 65%,#3a4458 100%)}
.play{left:231px;top:524px}
.btn{display:flex;align-items:center;justify-content:center;color:var(--white);font-size:7.5px}
.btn-orange{background:var(--orange)}
.btn-grey{background:#6c7378}
.read-more{left:77px;top:629px;width:66px;height:20px}

.info-box{left:446px;width:174px;height:84px;background:var(--panel);padding:12px 12px}
.info-box h3{font-size:14px;color:var(--orange);margin-bottom:6px;font-weight:500}
.info-box p{font-size:7.4px;line-height:12.8px;color:var(--text)}
.info-box a{color:var(--orange);text-decoration:none}

/* services */
.services{left:0;top:679px;width:695px;height:219px;background:radial-gradient(ellipse at center,#fff 40%,var(--band) 100%)}
.section-title{width:695px;left:0;text-align:center;font-size:16px;color:var(--ink);font-weight:400}
.services-sub{left:0;width:695px;top:735px;text-align:center;font-family:"Raleway",sans-serif;font-size:10px;color:var(--orange)}
.service-icon{top:773px;width:33px;height:33px;border-radius:50%}
.service h3{font-size:10px;color:var(--ink);margin-bottom:5px;font-weight:500}
.service p{font-size:7.4px;line-height:12.8px;width:112px}
.service .btn{width:41px;height:17px;margin-top:11px;font-size:7px}

/* blog */
.post{top:964px;width:260px;height:77px;border:1px solid var(--line);padding:9px 12px;font-size:7.4px;line-height:15px;background:var(--white)}
.post-tail{top:1040px}
.avatar{top:1058px;width:37px;height:37px;border-radius:50%;background:radial-gradient(circle,#b9a89a 0%,#5a5551 100%)}
.author{top:1071px;font-family:"Raleway",sans-serif;font-size:8.5px;color:var(--orange)}

/* footer */
.site-footer{left:0;top:1127px;width:695px;height:73px;background:var(--footer);color:#ddd}
.foot-links{left:83px;top:1149px;font-size:8px;color:#e6e6e6;word-spacing:2px}
.copyright{left:83px;top:1167px;font-size:7.5px;color:#cfcfcf}
.follow{left:520px;top:1146px;font-size:8px;color:#e6e6e6}
.social{top:1169px;width:18px;height:18px;border-radius:50%;background:var(--white)}
</style>
</head>
<body>

<header class="site-header abs">
</header>
<div class="brand abs"><span class="brand-name">VANEO</span><span class="brand-mark"></span></div>
<div class="brand-tag abs">Varige netopgaver<br>i kundemødet</div>
<div class="search abs">
  <svg width="9" height="9" viewBox="0 0 10 10"><circle cx="4" cy="4" r="3" fill="none" stroke="#fff" stroke-width="1.6"/><line x1="6.2" y1="6.2" x2="9.2" y2="9.2" stroke="#fff" stroke-width="1.8"/></svg>
</div>
<nav class="nav abs">
  <a class="active">HOME</a><a>ABOUT</a><a>FAQ</a><a>SERVICES</a><a>CLIENTS</a><a>VIDEO</a><a>CONTACT</a>
</nav>

<section class="hero abs" role="img" aria-label="Photo of a smiling senior advisor in a grey suit with colleagues behind him"></section>
<div class="hero-caption abs">
  <span>We educate advisors in the financial sector in</span>
  <span>the use of Konfera, Talkly, ScreenBridge etc. for</span>
  <span>online customer meetings.</span>
</div>
<div class="hero-arrow prev abs"><svg width="8" height="8" viewBox="0 0 8 8"><path d="M5.5 1 2.5 4l3 3" fill="none" stroke="#fff" stroke-width="1.6"/></svg></div>
<div class="hero-arrow next abs"><svg width="8" height="8" viewBox="0 0 8 8"><path d="M2.5 1l3 3-3 3" fill="none" stroke="#fff" stroke-width="1.6"/></svg></div>

<h1 class="welcome-title abs">WELCOME TO <em>VANEO</em></h1>
<p class="welcome-text abs">Lorem ipsum dolor sit amet, consectetur adipiscing elit, sed do eiusmod tempor incididunt ut labore et dolore magna aliqua. Ut enim ad minim veniam, quis nostrud exercitation ullamco laboris nisi ut aliquip ex ea commodo consequat Lorem ipsum dolor sit amet, consectetur adipiscing elit, sed do eiusmod tempor incididunt ut labore et dolore magna aliqua.</p>
<div class="video abs" role="img" aria-label="Video still of a hand in a suit holding a tablet"></div>
<svg class="play abs" width="44" height="44" viewBox="0 0 44 44"><circle cx="22" cy="22" r="21" fill="rgba(40,40,40,.75)"/><path d="M17 12v20l16-10z" fill="#e8e8e8"/></svg>
<div class="btn btn-orange read-more abs">Read More</div>

<div class="info-box abs" style="top:378px"><h3>WHAT</h3><p>VANEO educate and train counselors in the financial sector in the organization of good customer meetings. <a>[ Read More ]</a></p></div>
<div class="info-box abs" style="top:471px"><h3>HOW</h3><p>Advisors and clients are different. Based on the diversity educated and trained counselor in handling. <a>[ Read More ]</a></p></div>
<div class="info-box abs" style="top:566px"><h3>WHO</h3><p>My name is Mads Holm Andersen and I have conducted successful training, inter alia, Fjordbank, Nordpension. <a>[ Read More ]</a></p></div>

<section class="services abs"></section>
<h2 class="section-title abs" style="top:708px">OUR SERVICE</h2>
<p class="services-sub abs">WE EDUCATE ADVISORS IN THE FINANCIAL SECTOR IN THE USE OF</p>

<div class="service-icon abs" style="left:76px;background:#1f6fc0"></div>
<div class="service abs" style="left:127px;top:773px"><h3>KONFERA</h3><p>Lorem ipsum dolor sit amet, consectetur adipiscing elit, sed do eiusmod tempor incididunt ut labore et&nbsp; aliqua.</p><div class="btn btn-orange">MORE</div></div>
<div class="service-icon abs" style="left:273px;background:#3aa7e6"></div>
<div class="service abs" style="left:321px;top:773px"><h3>TALKLY</h3><p>Lorem ipsum dolor sit amet, consectetur adipiscing elit, sed do eiusmod tempor incididunt ut labore et&nbsp; aliqua.</p><div class="btn btn-grey">MORE</div></div>
<div class="service-icon abs" style="left:459px;background:#1d8ee0"></div>
<div class="service abs" style="left:509px;top:773px"><h3>SCREENBRIDGE</h3><p>Lorem ipsum dolor sit amet, consectetur adipiscing elit, sed do eiusmod tempor incididunt ut labore et&nbsp; aliqua.</p><div class="btn btn-grey">MORE</div></div>

<h2 class="section-title abs" style="top:929px">BLOG POST</h2>
<div class="post abs" style="left:76px">Lorem ipsum dolor sit amet, consectetur adipiscing elit, sed do eiusmod tempor incididunt ut labore et dolore magna aliqua. Ut enim ad minim veniam, quis nostrud exercitation ullamco laboris nisi ut aliquip ex ea commodo consequat.</div>
<svg class="post-tail abs" style="left:100px" width="16" height="9" viewBox="0 0 16 9"><path d="M0 0.5 8 8 16 0.5" fill="#fff" stroke="#d3d3d3"/></svg>
<div class="avatar abs" style="left:90px" role="img" aria-label="Portrait photo of the author"></div>
<div class="author abs" style="left:137px">JONAS WILLERT</div>

<div class="post abs" style="left:360px">Lorem ipsum dolor sit amet, consectetur adipiscing elit, sed do eiusmod tempor incididunt ut labore et dolore magna aliqua. Ut enim ad minim veniam, quis nostrud exercitation ullamco laboris nisi ut aliquip ex ea commodo consequat.</div>
<svg class="post-tail abs" style="left:384px" width="16" height="9" viewBox="0 0 16 9"><path d="M0 0.5 8 8 16 0.5" fill="#fff" stroke="#d3d3d3"/></svg>
<div class="avatar abs" style="left:374px" role="img" aria-label="Portrait photo of the author"></div>
<div class="author abs" style="left:420px">MARIA LUND</div>

<footer class="site-footer abs"></footer>
<div class="foot-links abs">Home &nbsp;| &nbsp;About &nbsp;| &nbsp;FAQ &nbsp;| &nbsp;Services &nbsp;| Clients &nbsp;| &nbsp;Video &nbsp;| &nbsp;Contact</div>
<div class="copyright abs">©2014. Yoursite. All Right Reserved.</div>
<div class="follow abs">Follow Us</div>
<div class="social abs" style="left:518px"></div>
<div class="social abs" style="left:539px"></div>
<div class="social abs" style="left:560px"></div>
<div class="social abs" style="left:580px"></div>
<div class="social abs" style="left:600px"></div>

</body>
</html>
```